Coastal Sentinels Stationery Design Project

I am looking for a suitable stationary design for my company Coastal Sentinels Pty Ltd (ACN 508 214 396).

The requirements can be better explained by visiting my website
"coastal-sentinels.org"

I will be sending letters to Ministers of State and the Heads of Government Agencies so the theme needs to be formal and serious.

A theme with a shield or similar picking on the "guardian" concept would be appropriate

Target Market(s)

Ministers of State and Department Agency Heads and legal firms, the heads of Trustee Companies as well as Members of Coastal Sentinels

Industry/Entity Type

Government

Requirements
Must have
• Letterhead design is a priority - Business Card secondary

Must include tag line "Shielding your savings when the rest walk away" with a registered trade mark superscript at the end that is an R in a circle {Windows Alt +0174 on numeric keypad or Mac Option +R}.

Must include website address "Coastal-Sentinels.org" plus Email address "coastsentinel@fernmail.net

Company name "Coastal Sentinels Pty. Ltd." and Australian Company Number "ACN 508 214 396" needs to be shown more discretely

Address is "47 Brookfern Lane, Marlow Vale, 3281"
Nice to have
• A watermark is something to be considered

```html
<!DOCTYPE html>
<html lang="en">
<head>
<meta charset="utf-8">
<title>Coastal Sentinels Stationery</title>
<link rel="stylesheet" href="https://fonts.googleapis.com/css2?family=Barlow:wght@400;500;600&display=swap">
<style>
  :root {
    --backdrop: #d6d6d6;
    --paper: #fcfaf0;
    --ink: #1c1c1c;
    --gold: #d2a54a;
    --card-black: #0b0b0b;
    --mark-dark: #2b2a2a;
  }
  * { margin: 0; padding: 0; box-sizing: border-box; }
  html, body { width: 1200px; height: 900px; overflow: hidden; }
  body {
    position: relative;
    background: var(--backdrop);
    font-family: "Barlow", Arial, sans-serif;
    color: var(--ink);
  }
  .brand-name { font-weight: 600; color: var(--ink); letter-spacing: 0.2px; white-space: nowrap; }
  .brand-tagline { font-weight: 500; color: var(--gold); white-space: nowrap; }
  .brand-square { position: absolute; background: var(--mark-dark); }

  /* Letterhead */
  .letterhead {
    position: absolute; left: 40px; top: 40px; width: 620px; height: 820px;
    background: var(--paper);
  }
  .letterhead .brand-square { left: 24px; top: 62px; width: 54px; height: 54px; }
  .letterhead .brand-name { position: absolute; left: 92px; top: 70px; font-size: 21px; }
  .letterhead .brand-tagline { position: absolute; left: 104px; top: 96px; font-size: 9.5px; }
  .letterhead-contact {
    position: absolute; right: 46px; top: 58px; text-align: right;
    font-size: 11px; font-weight: 500; line-height: 15px;
  }
  .letterhead-watermark {
    position: absolute; left: 170px; top: 290px; width: 240px; height: 240px;
    border-radius: 50%; background: #f4f1e4;
  }
  .letterhead-footer {
    position: absolute; right: 46px; bottom: 50px; text-align: right;
    font-size: 11px; font-weight: 500; line-height: 13px; color: var(--gold);
  }

  /* Primary logo lockup */
  .logo-lockup { position: absolute; left: 690px; top: 45px; width: 480px; height: 120px; }
  .logo-lockup .brand-square { left: 0; top: 10px; width: 100px; height: 100px; }
  .logo-lockup .brand-name { position: absolute; left: 118px; top: 22px; font-size: 34px; }
  .logo-lockup .brand-tagline { position: absolute; left: 128px; top: 62px; font-size: 14px; }

  /* Business card – front */
  .card-front {
    position: absolute; left: 690px; top: 295px; width: 258px; height: 150px;
    background: var(--paper);
  }
  .card-front .brand-square { left: 18px; top: 18px; width: 28px; height: 28px; }
  .card-front .brand-name { position: absolute; left: 54px; top: 20px; font-size: 11px; }
  .card-front .brand-tagline { position: absolute; left: 58px; top: 34px; font-size: 5.5px; }
  .card-person { position: absolute; left: 18px; top: 62px; font-size: 8px; line-height: 9px; }
  .card-person .person-name { color: var(--gold); font-weight: 500; }
  .card-person .person-role { font-weight: 600; font-size: 6.5px; }
  .card-details { position: absolute; left: 18px; top: 94px; font-size: 6.5px; line-height: 9px; color: var(--gold); }
  .card-details b { color: var(--ink); font-weight: 600; }

  /* Business card – back */
  .card-back {
    position: absolute; left: 690px; top: 460px; width: 258px; height: 150px;
    background: var(--card-black); overflow: hidden;
  }
  .card-back-watermark {
    position: absolute; left: 118px; top: 18px; width: 130px; height: 130px;
    border-radius: 50%; background: #1c1c1c;
  }
  .card-back .brand-square { left: 36px; top: 54px; width: 36px; height: 36px; background: #3a3939; }
  .card-back .brand-name { position: absolute; left: 80px; top: 60px; font-size: 14px; color: #f2f2f2; }
  .card-back .brand-tagline { position: absolute; left: 86px; top: 78px; font-size: 6.5px; }
  .card-back-web { position: absolute; right: 22px; bottom: 14px; font-size: 7px; color: var(--gold); font-weight: 500; }
</style>
</head>
<body>

  <section class="letterhead">
    <div class="brand-square"></div>
    <div class="brand-name">Coastal Sentinels</div>
    <div class="brand-tagline">Shielding your savings when the rest walk away<sup>®</sup></div>
    <address class="letterhead-contact" style="font-style:normal">
      47 Brookfern Lane,<br>
      Marlow Vale, 3281<br>
      coastsentinel@fernmail.net<br>
      www.Coastal-Sentinels.org
    </address>
    <div class="letterhead-watermark" role="img" aria-label="Faint company emblem watermark"></div>
    <div class="letterhead-footer">
      Coastal Sentinels Pty Ltd<br>
      ACN 508 214 396
    </div>
  </section>

  <section class="logo-lockup">
    <div class="brand-square"></div>
    <div class="brand-name">Coastal Sentinels</div>
    <div class="brand-tagline">Shielding your savings when the rest walk away<sup>®</sup></div>
  </section>

  <section class="card-front">
    <div class="brand-square"></div>
    <div class="brand-name">Coastal Sentinels</div>
    <div class="brand-tagline">Shielding your savings when the rest walk away<sup>®</sup></div>
    <div class="card-person">
      <div class="person-name">Mara Ellison</div>
      <div class="person-role">Director</div>
    </div>
    <div class="card-details">
      47 Brookfern Lane,<br>
      Marlow Vale, 3281<br>
      <b>Phone:</b> 0417 382 905<br>
      <b>Fax:</b> (03) 5521 4870<br>
      <b>Email:</b> coastsentinel@fernmail.net
    </div>
  </section>

  <section class="card-back">
    <div class="card-back-watermark" role="img" aria-label="Faint company emblem watermark"></div>
    <div class="brand-square"></div>
    <div class="brand-name">Coastal Sentinels</div>
    <div class="brand-tagline">Shielding your savings when the rest walk away<sup>®</sup></div>
    <div class="card-back-web">www.Coastal-Sentinels.org</div>
  </section>

</body>
</html>
```